Front book cover for a training course to help bakers get higher prices and sell more wedding cakes.

We need a front cover for a book that will be teaching bakers how to sell wedding cakes to get higher prices and book more orders. It is a business book. Do not make it look like we want brides to read it. Bakers will be judging the cover to see if it is worth their investment to read it. The title is already in the logo, so do not repeat it.

Target Market(s)

Bakers who sell wedding cakes

Industry/Entity Type

Bakery

Colors

Designer to choose colors to be used in the design.

Requirements
Must have
• Must use the logo. Must have author name: Lou Brand. Must have subtitle: Boost Your Prices. Book More Brides. Build Your Empire.
Nice to have
• You are free to be creative. The concept is not to be pretty. It is a business sales and marketing book

```html
<!DOCTYPE html>
<html lang="en">
<head>
<meta charset="utf-8">
<title>Book Cover – Lou Brand</title>
<link href="https://fonts.googleapis.com/css2?family=Bebas+Neue&family=Montserrat:wght@600;700&display=swap" rel="stylesheet">
<style>
  :root {
    --page-bg: #ffffff;
    --cover-yellow: #fbdc0a;
    --grid-line: rgba(150, 140, 90, 0.28);
    --band-blue: #0c5296;
    --ink-white: #ffffff;
    --ink-dark: #333333;
    --money-green: #3aa655;
    --money-light: #dcefd6;
    --cake-pink: #f3cfd3;
    --cake-mint: #e6f1ec;
  }
  * { box-sizing: border-box; margin: 0; padding: 0; }
  html, body {
    width: 1200px;
    height: 675px;
    overflow: hidden;
    background: var(--page-bg);
  }
  .canvas {
    position: relative;
    width: 1200px;
    height: 675px;
  }
  .cover {
    position: absolute;
    left: 380px;
    top: 26px;
    width: 440px;
    height: 622px;
    overflow: hidden;
    background-color: var(--cover-yellow);
    background-image:
      linear-gradient(var(--grid-line) 1px, transparent 1px),
      linear-gradient(90deg, var(--grid-line) 1px, transparent 1px);
    background-size: 19px 19px;
  }
  .bulb-icon {
    position: absolute;
    left: 100px;
    top: 118px;
    width: 64px;
    height: 72px;
  }
  .banknote-art {
    position: absolute;
    left: 350px;
    top: 0;
    width: 90px;
    height: 92px;
    border-radius: 0 0 0 40px;
    background: linear-gradient(135deg, var(--money-light), var(--money-green));
  }
  .growth-art {
    position: absolute;
    left: 252px;
    top: 316px;
    width: 174px;
    height: 206px;
    border-radius: 10px;
    background: linear-gradient(160deg, rgba(255,255,255,0.55), rgba(255,255,255,0.2));
  }
  .brand-badge {
    position: absolute;
    left: 165px;
    top: 25px;
    width: 110px;
    height: 110px;
    border-radius: 50%;
    background: var(--ink-white);
    display: flex;
    align-items: center;
    justify-content: center;
    text-align: center;
  }
  .brand-name {
    font-family: "Montserrat", sans-serif;
    font-weight: 700;
    font-size: 13px;
    line-height: 1.15;
    color: var(--ink-dark);
  }
  .cake-photo {
    position: absolute;
    left: 0;
    top: 184px;
    width: 242px;
    height: 341px;
    border-radius: 50% 50% 8px 8px / 30% 30% 8px 8px;
    background: linear-gradient(180deg, var(--cake-pink) 0%, var(--cake-mint) 45%, var(--cake-pink) 100%);
  }
  .subtitle {
    position: absolute;
    left: 182px;
    top: 192px;
    width: 258px;
    list-style: none;
  }
  .subtitle-line {
    height: 29px;
    margin-bottom: 9px;
    padding-left: 14px;
    padding-top: 1px;
    background: var(--band-blue);
    color: var(--ink-white);
    font-family: "Bebas Neue", sans-serif;
    font-size: 34px;
    line-height: 30px;
    white-space: nowrap;
    overflow: hidden;
  }
  .author-band {
    position: absolute;
    left: 0;
    bottom: 0;
    width: 440px;
    height: 39px;
    background: var(--band-blue);
    display: flex;
    align-items: center;
    justify-content: center;
  }
  .author-name {
    font-family: "Montserrat", sans-serif;
    font-weight: 700;
    font-size: 15px;
    letter-spacing: 1.5px;
    color: var(--ink-white);
    text-transform: uppercase;
  }
</style>
</head>
<body>
<main class="canvas">
  <article class="cover">
    <div class="banknote-art" role="img" aria-label="Illustration of a green dollar banknote tucked into the corner"></div>

    <svg class="bulb-icon" viewBox="0 0 64 72" aria-hidden="true">
      <g fill="none" stroke="var(--ink-white)" stroke-width="2.5" stroke-linecap="round">
        <path d="M22 48 a16 16 0 1 1 20 0 q-4 5 -4 10 h-12 q0 -5 -4 -10z"/>
        <line x1="27" y1="63" x2="37" y2="63"/>
        <line x1="29" y1="68" x2="35" y2="68"/>
        <line x1="32" y1="10" x2="32" y2="3"/>
        <line x1="12" y1="17" x2="7" y2="12"/>
        <line x1="52" y1="17" x2="57" y2="12"/>
        <line x1="6" y1="34" x2="0" y2="34"/>
        <line x1="58" y1="34" x2="64" y2="34"/>
      </g>
    </svg>

    <div class="cake-photo" role="img" aria-label="Photo of a three-tier white and pink wedding cake with cascading sugar roses"></div>

    <div class="growth-art" role="img" aria-label="Illustration of banknotes and rising arrows in hexagon frames over a wire mesh, with a small heart"></div>

    <div class="brand-badge">
      <span class="brand-name">Cake Profit<br>Coach</span>
    </div>

    <ul class="subtitle">
      <li class="subtitle-line">Boost Your Prices.</li>
      <li class="subtitle-line">Book More Brides.</li>
      <li class="subtitle-line">Build Your Empire.</li>
    </ul>

    <footer class="author-band">
      <span class="author-name">Lou Brand</span>
    </footer>
  </article>
</main>
</body>
</html>
```